Fernleaf Yards needs a brochure

I need to put together a booklet type brochure visually describing what I do. I would like the brochure to have the same elegance as the logo and the business card. I envision using the green design from the back of the business card, on the back of the brochure as well. I would like to have a space for an "About Us" area in which I can explain about the evolution of Fernleaf Yards. I would also like to have pictures of work that I have completed. I will send you both copy and photos. I would like the brochure to print matte and be an unusual shape - like a square booklet instead of the normal 8.5x11. I would also like to include the logos of the organizations that I am a member of - NHRO, TIMBER, KWOE.
Having some trouble uploading with internet explorer. Will fix the problem and upload ASAP. Thank you all for your patience.

```html
<!DOCTYPE html>
<html lang="en">
<head>
<meta charset="utf-8">
<title>Fernleaf Yards – Brochure Spread</title>
<link rel="stylesheet" href="https://fonts.googleapis.com/css2?family=Lato:wght@400;700&display=swap">
<style>
  :root {
    --leaf-green: #9cc531;
    --bark-brown: #8b5a34;
    --divider-brown: #9a5a2c;
    --ink: #1e1e1e;
    --paper: #ffffff;
    --paper-shade: #ececec;
    --foxglove: #8a8f6a;
    --gerbera: #3aa6b4;
    --planter: #4f5250;
    --calla: #e77a2a;
  }
  * { margin: 0; padding: 0; box-sizing: border-box; }
  html, body { width: 1200px; height: 599px; overflow: hidden; }
  body {
    font-family: "Lato", sans-serif;
    background: var(--paper);
  }
  .spread {
    position: relative;
    width: 1200px;
    height: 599px;
    overflow: hidden;
    background: linear-gradient(to bottom, var(--paper) 55%, var(--paper-shade) 100%);
  }
  .photo-strip {
    position: absolute;
    top: 0; left: 0;
    width: 1200px; height: 330px;
  }
  .photo {
    position: absolute;
    top: 0;
    height: 330px;
  }
  .photo--foxglove { left: 0; width: 297px; background: linear-gradient(160deg, #b79a86 0%, #6f7a52 45%, #4f6a34 70%, #c9c6d8 100%); }
  .photo--gerbera { left: 303px; width: 298px; background: radial-gradient(circle at 65% 30%, #e0407a 0%, #e8689a 18%, #4fb3c0 45%, var(--gerbera) 100%); }
  .photo--planter { left: 601px; width: 299px; background: linear-gradient(180deg, #a47a62 0%, #e4e6df 25%, var(--planter) 55%, #6e6a60 100%); }
  .photo--calla { left: 900px; width: 300px; background: radial-gradient(circle at 45% 30%, var(--calla) 0%, #f09a4e 35%, #f6efe6 75%, #ffffff 100%); }
  .photo-divider {
    position: absolute;
    top: 0; left: 297px;
    width: 6px; height: 330px;
    background: var(--divider-brown);
  }
  .wave {
    position: absolute;
    top: 0; left: 0;
    width: 1200px; height: 599px;
  }
  .wave .band { fill: var(--leaf-green); }
  .wave .base { fill: var(--paper); }
  .brand {
    position: absolute;
    left: 918px; top: 238px;
    width: 230px;
    text-align: center;
  }
  .brand__mark {
    display: block;
    width: 62px; height: 62px;
    margin: 0 auto 14px;
    border-radius: 50%;
    background: var(--leaf-green);
  }
  .brand__name {
    font-size: 30px;
    font-weight: 400;
    color: var(--bark-brown);
    line-height: 1;
  }
  .column {
    position: absolute;
    top: 380px;
    width: 550px;
  }
  .column--left { left: 26px; }
  .column--right { left: 639px; width: 535px; }
  .column__title {
    font-size: 31px;
    font-weight: 400;
    color: var(--bark-brown);
    line-height: 1.1;
    margin-bottom: 4px;
  }
  .column__body {
    font-size: 13px;
    line-height: 20.5px;
    color: var(--ink);
    text-align: justify;
  }
</style>
</head>
<body>
<main class="spread">
  <div class="photo-strip">
    <div class="photo photo--foxglove" role="img" aria-label="Garden bed with tall pink foxgloves, calla lilies and white pansies beside a brick building"></div>
    <div class="photo-divider"></div>
    <div class="photo photo--gerbera" role="img" aria-label="Close-up of bright pink gerbera daisies against a teal background"></div>
    <div class="photo photo--planter" role="img" aria-label="Dark square planters filled with white trailing flowers by a brick wall"></div>
    <div class="photo photo--calla" role="img" aria-label="Bouquet of orange calla lilies on white"></div>
  </div>

  <svg class="wave" viewBox="0 0 1200 599" aria-hidden="true">
    <path class="band" d="M0,258 C180,300 330,322 540,296 S930,212 1200,246 L1200,599 L0,599 Z"/>
    <path class="base" d="M0,282 C190,322 350,334 560,308 S940,238 1200,268 L1200,599 L0,599 Z"/>
  </svg>

  <div class="brand">
    <span class="brand__mark"></span>
    <p class="brand__name">Fernleaf Yards</p>
  </div>

  <section class="column column--left">
    <h2 class="column__title">Donec vitae rhoncus</h2>
    <p class="column__body">Lorem ipsum dolor sit amet, consectetur adipiscing elit. Nullam ornare porta dui. Praesent convallis risus at blandit eleifend. Nullam vulputate velit risus, a porttitor nulla elementum sed. Mauris elementum nibh eu imperdiet luctus. Pellentesque viverra posuere orci, id gravida metus aliquet a. Sed faucibus scelerisque sodales. Sed erat leo, faucibus volutpat tempor non, imperdiet sed tortor. Donec vitae rhoncus mauris. Donec tincidunt faucibus neque ac lobortis.</p>
  </section>

  <section class="column column--right">
    <h2 class="column__title">Phasellus laoreet</h2>
    <p class="column__body">Vestibulum in metus nunc. Class aptent taciti sociosqu ad litora torquent per conubia nostra, per inceptos himenaeos. Duis ut consectetur enim, eu feugiat arcu. Donec tempor tincidunt neque, ac lobortis mauris accumsan vitae. Nam libero erat, elementum a lectus non, pharetra viverra urna. Phasellus laoreet, velit pulvinar facilisis faucibus, ipsum lectus accumsan magna, sit amet hendrerit massa risus eu leo. Aliquam dapibus a quam pulvinar accumsan.</p>
  </section>
</main>
</body>
</html>
```